Quillbrook Cellars Winery… For non-interventionist winemakers, wine-making begins in the

Need a new website for my new winery…previous one lost in divorce to my cheating ex wife…sigh. Calling it Quillbrook Cellars. Want it to look like a wedding sight…calligraphy writing…black and white…with some black roses…want the look of a invitational wedding site…celebratory! We employ a combination of modern techniques and old world traditions, practicing both the cuvee and "field blending" methods, to create a range of distinctive varietals. To ensure flawless berries reach the fermentation process, we hand-sort grapes as soon as we get them into the winery. Our open-top, double-jacketed fermenters allow precise temperature control during "cold soak" periods and primary fermentation -- essential for color, flavor, and tannin extraction. Occasional délestage ("rack & return") aerates the wine. After ratchet basket pressing, we age our wines in French oak barrels for at least 18 months; minimal racking lets wine clarify naturally. Patience, sagacity, gumption, and a balance between both received methods (classic and modern) and ingenuity are foundations for crafting the world-class wines offered by our small, family-run artisanal winery here in the beautiful Larkspur Hollow valley, located beneath the Blue Mountains in eastern Washington

Target Market(s)

Wine drinkers/broken hearts

Industry/Entity Type

Winery

Number of Pages Required

4 page

Font styles to use
Script

Colors

Designer to choose only greyscale colors for use in the design.

Requirements
Must have
• Black roses… From our Larkspur Hollow valley boutique winery here in the Northern Highlands, we offer a range of premium reds, whites, ice wines, late harvest wines, brandies, grappas, and specialty spirits. We embrace sustainable farming methods on our estate vineyard and source fruit from growers who share our commitment to biodiversity. A great bottle of wine begins with the vine! For our "green wines," we practice innovative eco-friendly techniques, aim for Earth-friendly packaging, and donate a portion of our after-profit proceeds to environmental concerns. Though we appreciate ratings, we're less interested in numbers and more in the approval of our palettes and those of trusted friends, as well as accolades from loyal customers near and far. We handcraft what we hope will become your cult wines, often well into the night, humbled by the calls of barn owls who give our cellar its name.
Nice to have
• Page to list varieties…Wanderpeak Riesling, Moonthistle Sparkling, Dovemarrow Red

```html
<!DOCTYPE html>
<html lang="en">
<head>
<meta charset="utf-8">
<title>Quillbrook Cellars</title>
<link rel="stylesheet" href="https://fonts.googleapis.com/css2?family=Pinyon+Script&family=Raleway:wght@400;500&family=Quicksand:wght@500;600&display=swap">
<style>
:root{
  --ink:#3b3c3e;
  --charcoal:#505356;
  --text:#4a4a4a;
  --soft:#f4f4f4;
  --white:#ffffff;
  --line:#c9c9c9;
  --script:"Pinyon Script", cursive;
  --body:"Raleway", sans-serif;
  --ui:"Quicksand", sans-serif;
}
*{margin:0;padding:0;box-sizing:border-box}
html,body{width:1200px;height:3512px;overflow:hidden;background:var(--white)}
body{position:relative;font-family:var(--body);color:var(--text)}
.abs{position:absolute}
.script{font-family:var(--script);color:var(--ink);font-weight:400;-webkit-text-stroke:.6px var(--ink)}
.btn{position:absolute;display:flex;align-items:center;justify-content:center;background:var(--charcoal);color:var(--white);font-family:var(--body);font-weight:500;font-size:15px;border-radius:30px;border:none}
/* hero */
.hero-photo{left:0;top:0;width:1200px;height:700px;background:linear-gradient(100deg,#e6e8ee 0%,#e9e9ec 40%,#ddcbbd 62%,#c39a86 75%,#d8cfc9 90%,#e4e4e8 100%)}
.hero-wave{left:0;top:560px;width:1200px;height:160px}
.logo{font-family:var(--script);color:var(--ink);line-height:1}
.nav-logo{left:116px;top:22px;font-size:40px;width:180px;line-height:.85;text-align:center}
.nav{left:779px;top:54px;display:flex;gap:38px;font-family:var(--ui);font-weight:500;font-size:18px;color:var(--ink)}
.nav span{display:flex;align-items:center;gap:4px}
.welcome{left:110px;top:216px;font-size:40px}
.hero-title{left:110px;top:262px;font-size:70px;white-space:nowrap}
/* about */
.about-photo{left:139px;top:777px;width:412px;height:416px;border-radius:50%;background:radial-gradient(circle at 45% 40%,#c9a98e,#8c7358 55%,#5f5a3e);box-shadow:0 0 40px rgba(0,0,0,.06)}
.about-photo-small{left:382px;top:985px;width:205px;height:205px;border-radius:50%;background:radial-gradient(circle at 50% 55%,#8a2a2a,#3b1e1c 65%);border:6px solid var(--white)}
.about-title{left:642px;top:780px;font-size:50px}
.about-text{left:644px;top:864px;width:448px;font-size:15px;line-height:25.8px}
/* wine */
.wine-band{left:0;top:1270px;width:1200px;height:700px}
.roses-tl{left:0;top:1280px;width:395px;height:355px;background:radial-gradient(ellipse closest-side at 30% 40%,#5e6264,#7d8385 50%,rgba(125,131,133,0) 100%)}
.wine-title{left:0;top:1418px;width:1200px;text-align:center;font-size:50px}
.wine-item{position:absolute;top:1522px;width:300px;text-align:center}
.wine-photo{width:196px;height:196px;margin:0 auto;border-radius:50%;border:6px solid var(--charcoal)}
.wine-name{margin-top:12px;font-size:30px;white-space:nowrap}
/* black roses */
.roses-title{left:110px;top:1980px;font-size:50px}
.roses-text{left:110px;top:2068px;width:958px;font-size:15.4px;line-height:26.7px}
.roses-br{left:700px;top:2260px;width:500px;height:285px;background:radial-gradient(ellipse closest-side at 65% 55%,#4f5456,#6f7577 50%,rgba(111,117,119,0) 100%)}
.roses-r{left:1120px;top:2070px;width:80px;height:180px;background:radial-gradient(ellipse closest-side at 80% 50%,#c8cccd,rgba(200,204,205,0) 100%)}
/* contact */
.contact-bg{left:0;top:2420px;width:1200px;height:720px}
.contact-title{left:0;top:2552px;width:1200px;text-align:center;font-size:50px}
.field{position:absolute;height:57px;background:var(--white);border:1px solid var(--line);border-radius:30px;padding-left:27px;display:flex;align-items:center;font-family:var(--body);font-size:14px;color:var(--ink);box-shadow:0 2px 4px rgba(0,0,0,.08)}
.submit{font-family:var(--ui);font-size:17px;letter-spacing:.5px}
/* footer */
.footer-logo{left:0;top:3165px;width:1200px;text-align:center;font-size:70px;line-height:.85}
.footer-nav{left:0;top:3336px;width:1200px;display:flex;justify-content:center;gap:36px;font-family:var(--ui);font-weight:500;font-size:14px;color:var(--ink)}
.socials{left:0;top:3386px;width:1200px;display:flex;justify-content:center;gap:7px}
.socials span{width:36px;height:36px;border:1.5px solid var(--ink);border-radius:50%}
.copyright{left:0;top:3451px;width:1200px;text-align:center;font-family:var(--ui);font-weight:500;font-size:14px;color:var(--ink)}
.roses-bl{left:0;top:3310px;width:355px;height:202px;background:radial-gradient(ellipse closest-side at 45% 55%,#3f4244,#6a6e70 50%,rgba(106,110,112,0) 100%)}
</style>
</head>
<body>

<header>
  <div class="abs hero-photo" role="img" aria-label="Friends raising glasses of red and white wine in a toast against a bright sky"></div>
  <svg class="abs hero-wave" viewBox="0 560 1200 160" preserveAspectRatio="none" aria-hidden="true">
    <path d="M0 600 C150 575 300 585 420 640 C520 688 640 700 760 660 C860 620 920 585 1040 588 C1120 590 1170 610 1200 635 L1200 720 L0 720 Z" fill="#ffffff"/>
    <path d="M0 600 C150 575 300 585 420 640 C520 688 640 700 760 660 C860 620 920 585 1040 588 C1120 590 1170 610 1200 635" fill="none" stroke="#505356" stroke-width="6"/>
  </svg>
  <div class="abs logo nav-logo">Quillbrook<br>Cellars</div>
  <nav class="abs nav">
    <span>HOME</span>
    <span>WINE <svg width="12" height="9" viewBox="0 0 12 9"><path d="M1 1.5 6 7 11 1.5" fill="none" stroke="#3b3c3e" stroke-width="2.5"/></svg></span>
    <span>CONTACT US</span>
  </nav>
  <div class="abs script welcome">Welcome to</div>
  <h1 class="abs script hero-title">Quillbrook Cellars</h1>
  <div class="btn" style="left:112px;top:379px;width:140px;height:55px">Get Started</div>
</header>

<section class="about">
  <div class="abs about-photo" role="img" aria-label="Friends toasting with wine at a table in the vineyard"></div>
  <div class="abs about-photo-small" role="img" aria-label="Red wine being poured into a glass"></div>
  <h2 class="abs script about-title">About Us</h2>
  <p class="abs about-text">We employ a combination of modern techniques and old world traditions, practicing both the cuvee and "field blending" methods, to create a range of distinctive varietals. To ensure flawless berries reach the fermentation process, we hand-sort grapes as soon as we get them into the winery. Our open-top, double-jacketed fermenters allow precise temperature control during "cold soak" periods and primary fermentation -- essential for color, flavor, and tannin extraction. Occasional délestage ("rack &amp; return") aerates the wine.</p>
  <div class="btn" style="left:644px;top:1122px;width:140px;height:55px">Learn More</div>
</section>

<section class="wine">
  <svg class="abs wine-band" viewBox="0 1270 1200 700" preserveAspectRatio="none" aria-hidden="true">
    <path d="M0 1282 C300 1270 600 1420 1000 1398 C1100 1392 1160 1365 1200 1345 L1200 1922 C1050 1975 800 1972 550 1902 C380 1852 200 1845 0 1922 Z" fill="#f4f4f4"/>
  </svg>
  <div class="abs roses-tl" role="img" aria-label="Grey roses and leaves"></div>
  <h2 class="abs script wine-title">Wine</h2>
  <div class="wine-item" style="left:157px">
    <div class="wine-photo" role="img" aria-label="White wine glass beside green grape clusters" style="background:radial-gradient(circle at 55% 50%,#9ab34a,#4d6b25 60%,#2f4418)"></div>
    <div class="script wine-name">Wanderpeak Riesling</div>
  </div>
  <div class="wine-item" style="left:450px">
    <div class="wine-photo" role="img" aria-label="Stacked wine bottles in a cellar" style="background:radial-gradient(circle at 50% 60%,#6b4a2a,#2a1e18 60%,#151010)"></div>
    <div class="script wine-name">Moonthistle Sparkling</div>
  </div>
  <div class="wine-item" style="left:743px">
    <div class="wine-photo" role="img" aria-label="Red wine poured into a glass" style="background:radial-gradient(circle at 45% 60%,#8e1f2a,#b5785a 60%,#c9a184)"></div>
    <div class="script wine-name">Dovemarrow Red</div>
  </div>
</section>

<section class="black-roses">
  <h2 class="abs script roses-title">Black Roses</h2>
  <p class="abs roses-text">Black roses… From our Larkspur Hollow valley boutique winery here in the Northern Highlands, we offer a range of premium reds, whites, ice wines, late harvest wines, brandies, grappas, and specialty spirits. We embrace sustainable farming methods on our estate vineyard and source fruit from growers who share our commitment to biodiversity. A great bottle of wine begins with the vine! For our "green wines," we practice innovative eco-friendly techniques, aim for Earth-friendly packaging, and donate a portion of our after-profit proceeds to environmental concerns. Though we appreciate ratings, we're less interested in numbers and more in the approval of our palettes and those of trusted friends, as well as accolades from loyal customers near and far. We handcraft what we hope will become your cult wines, often well into the night, humbled by the calls of barn owls who give our cellar its name.</p>
  <div class="btn" style="left:110px;top:2283px;width:141px;height:55px">Learn More</div>
  <div class="abs roses-r" role="img" aria-label="Pale rose stems"></div>
</section>

<section class="contact">
  <svg class="abs contact-bg" viewBox="0 2420 1200 720" role="img" aria-label="Softly faded photo of wine glasses on a dinner table" preserveAspectRatio="none">
    <defs>
      <linearGradient id="tableTone" x1="0" y1="0" x2="1" y2="1">
        <stop offset="0" stop-color="#e6e2de"/>
        <stop offset=".5" stop-color="#dcd7d2"/>
        <stop offset="1" stop-color="#e9e6e3"/>
      </linearGradient>
    </defs>
    <path d="M0 2482 C100 2440 200 2425 320 2430 C550 2440 800 2520 1200 2470 L1200 3123 C1000 3135 800 3120 600 3070 C420 3025 250 3030 0 3085 Z" fill="url(#tableTone)"/>
  </svg>
  <div class="abs roses-br" role="img" aria-label="Dark grey roses with leaves"></div>
  <h2 class="abs script contact-title">Contact Us</h2>
  <div class="field" style="left:170px;top:2663px;width:421px">First Name :</div>
  <div class="field" style="left:609px;top:2663px;width:421px">Last Name :</div>
  <div class="field" style="left:170px;top:2743px;width:421px">Email :</div>
  <div class="field" style="left:609px;top:2743px;width:421px">Phone :</div>
  <div class="field" style="left:170px;top:2827px;width:859px">Message :</div>
  <div class="btn submit" style="left:515px;top:2921px;width:168px;height:55px">SUBMIT</div>
</section>

<footer>
  <div class="abs roses-bl" role="img" aria-label="Two black roses"></div>
  <div class="abs logo footer-logo">Quillbrook<br>Cellars</div>
  <nav class="abs footer-nav"><span>HOME</span><span>WINE</span><span>CONTACT US</span></nav>
  <div class="abs socials" aria-label="Social links"><span></span><span></span><span></span><span></span><span></span></div>
  <p class="abs copyright">©Copyrights 2024 Company Name &nbsp;|&nbsp;&nbsp; All Rights Reserved</p>
</footer>

</body>
</html>
```